Tire trade

Hello, I would like to make A5 flyers for my garage, with the 'bramel tires' logo.
Registration: Sale and fitting of tires of all brands (also ordered by you) Guarding of your tires

Target Market(s)

All motorists in my area

Industry/Entity Type

Vente de pneus

Font styles to use
Serif

Colors
EE7325
F08F49
F5BC92
FAE3D3
FDF4ED

Requirements
Must have
• My logo, the place (Val-d'Illiez)
Nice to have
• Simple and eye-catching
Should not have
• pink

```html
<!DOCTYPE html>
<html lang="en">
<head>
<meta charset="utf-8">
<title>Bramel pneus – Tire offer flyer</title>
<link rel="stylesheet" href="https://fonts.googleapis.com/css2?family=Roboto+Slab:wght@700;800;900&family=Merriweather:wght@400;700&display=swap">
<style>
  :root{
    --cream:#FEF5F2;
    --amber:#FAAF2E;
    --tangerine:#F7922A;
    --rust:#BE4F27;
    --ink:#1F2433;
    --white:#FFFFFF;
    --slab:"Roboto Slab", serif;
    --text:"Merriweather", serif;
  }
  html,body{margin:0;padding:0;overflow:hidden;background:var(--cream);}
  .flyer{position:relative;width:839px;height:1200px;overflow:hidden;background:var(--cream);}
  .backdrop{position:absolute;inset:0;width:839px;height:1200px;}
  .abs{position:absolute;margin:0;}

  .top-contact{right:34px;top:18px;display:flex;align-items:center;gap:26px;
    font-family:var(--text);font-size:16px;color:var(--ink);line-height:1;}
  .top-contact .item{display:flex;align-items:center;gap:10px;}
  .top-contact svg{width:22px;height:22px;flex:none;}

  .brand{left:596px;top:112px;width:170px;height:160px;}
  .brand-ring{position:absolute;left:12px;top:0;width:146px;height:146px;border:4px solid var(--white);border-radius:50%;box-sizing:border-box;}
  .brand-name{position:absolute;left:0;top:38px;width:170px;text-align:center;
    font-family:var(--slab);font-weight:800;color:var(--white);font-size:30px;line-height:30px;}
  .brand-phone{position:absolute;left:0;top:101px;width:170px;text-align:center;
    font-family:var(--slab);font-weight:800;color:var(--white);font-size:15px;line-height:1;}

  .offer-badge{left:431px;top:544px;width:134px;height:134px;border-radius:50%;
    background:linear-gradient(90deg,var(--tangerine),#EE7325);
    font-family:var(--slab);font-weight:800;color:var(--ink);text-align:center;}
  .offer-badge .small{position:absolute;left:0;right:0;top:28px;font-size:18px;line-height:1;}
  .offer-badge .big{position:absolute;left:0;right:0;top:52px;font-size:27px;line-height:29px;}

  .discount{left:500px;top:648px;width:292px;text-align:center;
    font-family:var(--slab);font-weight:700;font-size:56px;letter-spacing:-1px;color:var(--white);line-height:1;}

  .headline{left:470px;top:742px;width:352px;text-align:center;
    font-family:var(--slab);font-weight:900;color:var(--ink);font-size:64px;line-height:70px;}

  .tagline{left:490px;top:886px;width:312px;text-align:center;
    font-family:var(--text);font-weight:700;font-size:29px;line-height:39px;color:var(--ink);}
  .tagline .accent{color:var(--rust);}

  .website{left:46px;top:1064px;font-family:var(--text);color:var(--ink);}
  .website .url{font-size:19px;line-height:1;}
  .website .cta{margin-top:10px;font-family:var(--slab);font-weight:800;font-size:23px;letter-spacing:3.5px;line-height:1;}

  .more-info{right:121px;top:1065px;text-align:right;font-family:var(--text);color:var(--white);}
  .more-info .label{font-weight:700;font-size:23px;line-height:1.1;}
  .more-info .phone{font-size:19px;line-height:1.3;}
  .chat-icon{left:732px;top:1066px;width:48px;height:48px;}
</style>
</head>
<body>
<div class="flyer">
  <svg class="backdrop" viewBox="0 0 839 1200">
    <defs>
      <linearGradient id="smokeTone" x1="0" y1="0" x2="1" y2="1">
        <stop offset="0" stop-color="#4A5964"/>
        <stop offset="0.5" stop-color="#5E7482"/>
        <stop offset="1" stop-color="#AFC3D0"/>
      </linearGradient>
      <radialGradient id="tireTone" cx="0.45" cy="0.4" r="0.7">
        <stop offset="0" stop-color="#3C3C3E"/>
        <stop offset="1" stop-color="#161618"/>
      </radialGradient>
    </defs>

    <polygon points="0,0 241,0 241,39 0,39" fill="var(--amber)"/>

    <polygon points="0,39 290,39 667,379 314,858 0,858" fill="url(#smokeTone)"
      role="img" aria-label="Photograph of a winter tire surrounded by smoke"/>

    <polygon points="366,64 839,64 839,313 646,313" fill="var(--rust)"/>
    <polygon points="677,360 785,360 785,457" fill="var(--amber)"/>

    <polygon points="648,405 839,578 839,1029 518,1029 324,837" fill="var(--amber)"/>
    <polygon points="718,476 839,578 839,664 671,541" fill="var(--tangerine)" opacity="0.6"/>
    <polygon points="751,560 839,637 839,727 705,625" fill="var(--tangerine)" opacity="0.6"/>

    <polygon points="0,863 330,863 387,1029 0,1029" fill="var(--rust)"/>

    <rect x="8" y="606" width="448" height="394" rx="26" fill="url(#tireTone)"
      role="img" aria-label="Photograph of a stack of new car tires"/>

    <polygon points="0,1029 384,1029 510,1151 0,1151" fill="var(--amber)"/>
    <polygon points="471,1029 839,1029 839,1151 530,1151 440,1067" fill="var(--rust)"/>
    <polygon points="0,1151 530,1151 585,1200 0,1200" fill="var(--rust)"/>
    <polygon points="654,1151 839,1151 839,1164 668,1164" fill="var(--amber)"/>
  </svg>

  <div class="abs top-contact">
    <span class="item">
      <svg viewBox="0 0 24 24" aria-hidden="true"><path d="M12,22 C12,22 5,14 5,9 A7,7 0 0 1 19,9 C19,14 12,22 12,22 Z" fill="none" stroke="var(--rust)" stroke-width="1.6"/><circle cx="12" cy="9" r="2.6" fill="none" stroke="var(--rust)" stroke-width="1.6"/></svg>
      Val-d'Illiez
    </span>
    <span class="item">
      <svg viewBox="0 0 24 22" aria-hidden="true"><path d="M2,12 L23,2 L15,20 L11,13 Z M11,13 L23,2 M4,19 L8,15 M2,16 L6,13" fill="none" stroke="var(--rust)" stroke-width="1.3" stroke-linejoin="round"/></svg>
      info@bramelpneus.com
    </span>
  </div>

  <div class="abs brand">
    <div class="brand-ring"></div>
    <div class="brand-name">Bramel<br>pneus</div>
    <div class="brand-phone">079/555.01.23</div>
  </div>

  <div class="abs offer-badge">
    <span class="small">BUY 4</span>
    <span class="big">GET 1<br>FREE !</span>
  </div>

  <p class="abs discount">-50%</p>

  <h1 class="abs headline">GET YOUR<br>TIRE</h1>

  <p class="abs tagline"><span class="accent">Always Ready...</span> All Brand!</p>

  <div class="abs website">
    <div class="url">www.bramelpneus.com</div>
    <div class="cta">VISIT OUR WEBSITE</div>
  </div>

  <div class="abs more-info">
    <div class="label">More info</div>
    <div class="phone">+000 123 456 789</div>
  </div>

  <svg class="abs chat-icon" viewBox="0 0 48 48" aria-hidden="true">
    <path d="M26,4 C37,4 45,11 45,20 C45,27 41,31 44,37 C38,37 35,35 32,34 C29,35 27,35 26,35 C15,35 7,28 7,20 C7,11 15,4 26,4 Z" fill="none" stroke="var(--white)" stroke-width="3" stroke-linejoin="round"/>
    <path d="M8,24 C4,30 4,36 2,43 C7,42 11,41 14,39 C18,41 22,41 25,40" fill="none" stroke="var(--white)" stroke-width="3" stroke-linecap="round" stroke-linejoin="round"/>
    <path d="M17,14 H35 M17,20 H35 M17,26 H29" stroke="var(--white)" stroke-width="3" stroke-linecap="round"/>
  </svg>
</div>
</body>
</html>
```